Lagoon Canopy NZ Product Catalogue

To redesign our suppliers catalogue and make it my own.
Verdmont is our supplier, although now I want a "Lagoon Canopy NZ" catalogue, with an updated look as well.

I have attached our logos, Verdmont catalogue and a few photos of completed work (which may need editing to look better).

Also pages I want to use from the catalogue (be similar to) are page numbers:
10 - 21 (products we sell)
It will also need a cover and contents page and a commercial enclosure page after the other products (with commercial 1 and 20130422_1 photos).

The first page as you open the catalogue I want the about us section of our website on there www.lagooncanopy.co.nz (two sections "what we offer" and "enclosure advantages")

If you need better photos or more information please contact me on:
tamsin@lagooncanopy.co.nz

Contact details: Toll Free 0508 SHELTERS (748 219) Email sales@lagooncanopy.co.nz

Industry/Entity Type

Construction

Colors

Designer to choose colors to be used in the design.

Requirements
Must have
• Must have double sided pages,
• With each different design to have two pages which open together.
• The standard sizing which is in the Verdmont Catalogue must be there.
• Designs are: Rivelle Horizon, Rivelle, Tormel, Quarry, Lisbet and Vale Shelters
• Must be printable and pdf sendable.
• Use "What we offer" and "Enclosure Advantages" to the first page customer opens to, maybe also a contents page.
• Also please add to the "enclosure advantages" bullet point list "Year-round average of 8 degree warmer water"
Nice to have
• Would be nice to have the custom sizing box as well on the designs asked for.
• Also a Commercial section after the rest of the designs using the "commercial 1" and "20130422_1" photos
• The more photos the better
• Be nice to be high resolution and I want to print it in a gloss finish.
• Also A4 size would be nice, but A5 will work also
Should not have
• Rivelle Horizon Neo and try and minimise the Verdmont branding

```html
<!DOCTYPE html>
<html lang="en">
<head>
<meta charset="utf-8">
<title>Lagoon Canopy NZ — Catalogue Spreads</title>
<link rel="stylesheet" href="https://fonts.googleapis.com/css2?family=Montserrat:wght@400;500;600;800&family=Oswald:wght@300;400;500&family=Raleway:wght@300;400&display=swap">
<style>
  :root{
    --stage-light:#6a6a6a;
    --stage-dark:#3b3b3b;
    --label:#b9b9b9;
    --paper:#ffffff;
    --paper-soft:#f0f0f0;
    --ghost:#e4e4e4;
    --brand-blue:#1f6fb5;
    --accent-blue:#3f8dca;
    --ink:#2b2b2b;
    --ink-soft:#5a5a5a;
    --navy-box:rgba(8,18,38,0.86);
    --white:#ffffff;
  }
  *{box-sizing:border-box;margin:0;padding:0}
  html,body{width:1200px;height:2296px;overflow:hidden}
  body{
    position:relative;
    background:radial-gradient(ellipse at 50% 45%,var(--stage-light) 0%,var(--stage-dark) 100%);
    font-family:"Montserrat",sans-serif;
  }
  .spread{position:absolute;left:112px;width:944px;height:671px;overflow:hidden;background:var(--paper);box-shadow:0 4px 14px rgba(0,0,0,.35)}
  .spread--outside{top:73px}
  .spread--inside-one{top:804px}
  .spread--inside-two{top:1538px;height:670px}

  .spread-label{
    position:absolute;left:1098px;width:44px;
    writing-mode:vertical-rl;transform:rotate(180deg);
    font-family:"Raleway",sans-serif;font-weight:300;font-size:36px;letter-spacing:3px;color:var(--label);
  }
  .spread-label--outside{top:535px}
  .spread-label--inside-one{top:1243px}
  .spread-label--inside-two{top:1995px}

  .photo{position:absolute}

  /* page halves */
  .page-left{position:absolute;left:0;top:0;width:472px;height:100%;background:linear-gradient(90deg,var(--paper-soft),#fbfbfb)}
  .ghost-name{
    position:absolute;left:32px;top:28px;height:615px;
    writing-mode:vertical-rl;transform:rotate(180deg);
    font-family:"Montserrat",sans-serif;font-weight:800;font-size:52px;letter-spacing:4px;color:var(--ghost);
    text-align:center;
  }

  /* outside */
  .contact{position:absolute;left:128px;top:290px;width:200px;text-align:center;font-family:"Raleway",sans-serif;color:var(--ink-soft)}
  .contact-title{font-family:"Montserrat",sans-serif;font-size:12px;font-weight:600;color:var(--ink)}
  .contact-title span{color:var(--accent-blue)}
  .contact-icons{display:flex;justify-content:center;gap:6px;margin:16px 0 14px}
  .contact-line{font-size:12.5px;line-height:17px}
  .tile-pattern{position:absolute;left:150px;top:465px}

  .brand{position:absolute;left:560px;top:44px;display:flex;align-items:center;gap:10px}
  .brand-name{font-family:"Montserrat",sans-serif;font-weight:800;font-size:29px;color:var(--brand-blue);letter-spacing:.5px}
  .brand-dot{width:14px;height:14px;border-radius:50%;background:var(--brand-blue)}

  .photo--cover{left:340px;top:129px;width:604px;height:402px;background:linear-gradient(160deg,#58c4e3 0%,#2aa5d4 45%,#1d86bd 100%)}
  .photo-notch{position:absolute;left:331px;top:322px;width:20px;height:36px;border-radius:0 18px 18px 0;background:var(--paper-soft)}

  .cover-headline{position:absolute;left:500px;top:548px;width:430px;text-align:center}
  .cover-title{font-family:"Oswald",sans-serif;font-weight:400;font-size:30px;letter-spacing:.5px;color:var(--accent-blue);line-height:36px}
  .cover-sub{font-family:"Raleway",sans-serif;font-weight:400;font-size:13px;color:var(--ink);margin-top:2px}
  .cover-web{position:absolute;left:600px;top:636px;font-family:"Raleway",sans-serif;font-size:11px;letter-spacing:2.5px;color:#8a8a8a}

  /* inside one */
  .inside-one .page-left{background:var(--paper)}
  .photo--contents-top{left:151px;top:0;width:321px;height:63px;background:linear-gradient(180deg,#d8d8d8,#8f8f8f 60%,#b5b5b5)}
  .photo--contents-bottom{left:151px;top:574px;width:321px;height:97px;background:linear-gradient(160deg,#5ab7df,#1f82c0 70%,#2a6fa8)}
  .contents-title{position:absolute;left:151px;top:82px;width:321px;text-align:center;font-family:"Oswald",sans-serif;font-weight:300;font-size:25px;color:var(--accent-blue)}
  .contents-list{position:absolute;left:153px;top:158px;width:290px;list-style:none}
  .contents-item{display:flex;justify-content:space-between;font-size:11px;color:var(--ink);height:35.2px;line-height:18px}

  .photo--feature{left:472px;top:0;width:472px;height:444px;background:linear-gradient(180deg,#e6eef2 0%,#cfdde4 12%,#355f31 26%,#2d5528 44%,#8b8f88 50%,#2d9ed0 58%,#4cbbe2 85%,#3aa7d4 100%)}
  .feature-heading{position:absolute;left:492px;top:372px;font-family:"Montserrat",sans-serif;font-weight:800;font-size:21px;line-height:22px;color:var(--white)}
  .feature-copy{position:absolute;left:492px;top:465px;width:433px}
  .body-copy{font-size:8.6px;line-height:11.5px;color:var(--ink);text-align:justify;margin-bottom:10px}

  /* inside two */
  .photo--night{left:0;top:0;width:944px;height:670px;background:linear-gradient(180deg,#0e1a33 0%,#1b2b47 28%,#3a3230 46%,#6a4a2c 55%,#3e4a40 66%,#2b4a3a 76%,#2fb4c2 88%,#1f6f82 100%)}
  .frame-line{position:absolute;left:23px;top:23px;width:898px;height:598px;border:1.5px solid rgba(255,255,255,.85)}
  .text-panel{position:absolute;background:var(--navy-box);padding:20px 15px 10px 14px;color:var(--white)}
  .text-panel--upper{left:615px;top:0;width:308px;height:329px;padding-top:22px}
  .text-panel--lower{left:23px;top:337px;width:306px;height:333px}
  .panel-heading{font-family:"Montserrat",sans-serif;font-weight:800;font-size:19px;line-height:20px;margin-bottom:10px}
  .text-panel .body-copy{color:#e8ecf2;font-size:7.6px;line-height:10.2px;margin-bottom:8px}
</style>
</head>
<body>

  <!-- Outside spread -->
  <section class="spread spread--outside" aria-label="Outside cover spread">
    <div class="page-left">
      <div class="ghost-name" aria-hidden="true">LAGOON CANOPY NZ</div>
      <div class="contact">
        <p class="contact-title"><span>CONTACT</span> US</p>
        <div class="contact-icons">
          <svg width="16" height="16" viewBox="0 0 16 16"><circle cx="8" cy="8" r="6.5" fill="none" stroke="#5a5a5a" stroke-width="1"/></svg>
          <svg width="16" height="16" viewBox="0 0 16 16"><circle cx="8" cy="8" r="6.5" fill="none" stroke="#5a5a5a" stroke-width="1"/><rect x="4.5" y="5.5" width="7" height="5" fill="none" stroke="#5a5a5a" stroke-width=".9"/><path d="M4.5 5.5 L8 8.5 L11.5 5.5" fill="none" stroke="#5a5a5a" stroke-width=".9"/></svg>
          <svg width="16" height="16" viewBox="0 0 16 16"><circle cx="8" cy="8" r="6.5" fill="none" stroke="#5a5a5a" stroke-width="1"/></svg>
        </div>
        <p class="contact-line">0219 486 205</p>
        <p class="contact-line">tamsin@lagooncanopy.co.nz</p>
        <p class="contact-line">www.lagooncanopy.co.nz</p>
      </div>
      <svg class="tile-pattern" width="200" height="160" viewBox="0 0 200 160" aria-hidden="true">
        <g fill="none" stroke="#dcdcdc" stroke-width="1.2">
          <rect x="40" y="50" width="58" height="58"/>
          <rect x="108" y="20" width="26" height="26"/>
          <rect x="112" y="62" width="52" height="52"/>
          <rect x="22" y="40" width="14" height="14"/>
          <rect x="170" y="40" width="18" height="18"/>
          <rect x="4" y="60" width="10" height="10"/>
          <rect x="146" y="0" width="20" height="20"/>
        </g>
      </svg>
    </div>
    <div class="brand">
      <span class="brand-name">LAGOON CANOPY NZ</span>
      <span class="brand-dot"></span>
    </div>
    <div class="photo photo--cover" role="img" aria-label="Photo of a child floating on a striped kickboard in a blue pool"></div>
    <div class="photo-notch"></div>
    <div class="cover-headline">
      <h1 class="cover-title">INCREASED WATER TEMPERATURE</h1>
      <p class="cover-sub">Free Heating From The Sun, Providing Significant Savings</p>
    </div>
    <p class="cover-web">www.lagooncanopy.co.nz</p>
  </section>
  <p class="spread-label spread-label--outside">OUTSIDE</p>

  <!-- Inside spread one -->
  <section class="spread spread--inside-one inside-one" aria-label="Contents and feature spread">
    <div class="page-left">
      <div class="ghost-name" aria-hidden="true">LAGOON CANOPY NZ</div>
    </div>
    <div class="photo photo--contents-top" role="img" aria-label="Black and white photo of an enclosure roof detail"></div>
    <h2 class="contents-title">TABLE OF CONTENTS</h2>
    <ul class="contents-list">
      <li class="contents-item"><span>Lorem Ipsum is a simply dummy text</span><span>00</span></li>
      <li class="contents-item"><span>Lorem Ipsum is a simply dummy text</span><span>00</span></li>
      <li class="contents-item"><span>Lorem Ipsum is a simply dummy text</span><span>00</span></li>
      <li class="contents-item"><span>Lorem Ipsum is a simply dummy text</span><span>00</span></li>
      <li class="contents-item"><span>Lorem Ipsum is a simply dummy text</span><span>00</span></li>
      <li class="contents-item"><span>Lorem Ipsum is a simply dummy text</span><span>00</span></li>
      <li class="contents-item"><span>Lorem Ipsum is a simply dummy text</span><span>00</span></li>
      <li class="contents-item"><span>Lorem Ipsum is a simply dummy text</span><span>00</span></li>
      <li class="contents-item"><span>Lorem Ipsum is a simply dummy text</span><span>00</span></li>
      <li class="contents-item"><span>Lorem Ipsum is a simply dummy text</span><span>00</span></li>
    </ul>
    <div class="photo photo--contents-bottom" role="img" aria-label="Photo of a child splashing in a pool"></div>

    <div class="photo photo--feature" role="img" aria-label="Photo of a low pool enclosure beside a deck with trees behind"></div>
    <h2 class="feature-heading">LOREM IPSUM IS<br>SIMPLY DUMMY TEXT</h2>
    <div class="feature-copy">
      <p class="body-copy">A retractable enclosure keeps leaves, dust and insects out of the water while letting the sun warm it through the day. The low profile panels slide away by hand in moments, so the pool opens fully on hot afternoons and closes again at dusk, holding heat overnight and cutting the cost of chemicals, cleaning and heating through every season.</p>
      <p class="body-copy">A retractable enclosure keeps leaves, dust and insects out of the water while letting the sun warm it through the day. The low profile panels slide away by hand in moments, so the pool opens fully on hot afternoons and closes again at dusk, holding heat overnight and cutting the cost of chemicals, cleaning and heating through every season.</p>
      <p class="body-copy">A retractable enclosure keeps leaves, dust and insects out of the water while letting the sun warm it through the day. The low profile panels slide away by hand in moments, so the pool opens fully on hot afternoons and closes again at dusk, holding heat overnight and cutting the cost of chemicals, cleaning and heating through every season.</p>
    </div>
  </section>
  <p class="spread-label spread-label--inside-one">INSIDE 1</p>

  <!-- Inside spread two -->
  <section class="spread spread--inside-two" aria-label="Night feature spread">
    <div class="photo photo--night" role="img" aria-label="Night photo of a lit house with a glowing enclosed pool in front"></div>
    <div class="frame-line" aria-hidden="true"></div>
    <div class="text-panel text-panel--upper">
      <h2 class="panel-heading">LOREM IPSUM IS<br>SIMPLY DUMMY TEXT</h2>
      <p class="body-copy">A retractable enclosure keeps leaves, dust and insects out of the water while letting the sun warm it through the day. The low profile panels slide away by hand in moments, so the pool opens fully on hot afternoons and closes again at dusk, holding heat overnight and cutting the cost of chemicals, cleaning and heating through every season.</p>
      <p class="body-copy">A retractable enclosure keeps leaves, dust and insects out of the water while letting the sun warm it through the day. The low profile panels slide away by hand in moments, so the pool opens fully on hot afternoons and closes again at dusk, holding heat overnight and cutting the cost of chemicals, cleaning and heating through every season.</p>
      <p class="body-copy">A retractable enclosure keeps leaves, dust and insects out of the water while letting the sun warm it through the day. The low profile panels slide away by hand in moments, so the pool opens fully on hot afternoons and closes again at dusk, holding heat overnight and cutting the cost of chemicals, cleaning and heating through every season.</p>
    </div>
    <div class="text-panel text-panel--lower">
      <h2 class="panel-heading">LOREM IPSUM IS<br>SIMPLY DUMMY TEXT</h2>
      <p class="body-copy">A retractable enclosure keeps leaves, dust and insects out of the water while letting the sun warm it through the day. The low profile panels slide away by hand in moments, so the pool opens fully on hot afternoons and closes again at dusk, holding heat overnight and cutting the cost of chemicals, cleaning and heating through every season.</p>
      <p class="body-copy">A retractable enclosure keeps leaves, dust and insects out of the water while letting the sun warm it through the day. The low profile panels slide away by hand in moments, so the pool opens fully on hot afternoons and closes again at dusk, holding heat overnight and cutting the cost of chemicals, cleaning and heating through every season.</p>
      <p class="body-copy">A retractable enclosure keeps leaves, dust and insects out of the water while letting the sun warm it through the day. The low profile panels slide away by hand in moments, so the pool opens fully on hot afternoons and closes again at dusk, holding heat overnight and cutting the cost of chemicals, cleaning and heating through every season.</p>
    </div>
  </section>
  <p class="spread-label spread-label--inside-two">INSIDE 2</p>

</body>
</html>
```